Need simple and modern looking business card with all my information on one side and logo on the other side
Info :
Company name - VELMAR CONSTRUCTION LLC
Company addres- 418 harbor 87th. Dunmoor park ny 10352
Email- velmarllc@tridomail.Com
Company phone number 555-318-6094
Cell number- 555-742-0583
Web site - velmarllc.Com
My name Gerald tomasino

Target Market(s)

Construction , home improvement, remodeling

Industry/Entity Type

Construction

Contact Information for Business Card

It has to be moder but at the same time simple

Font styles to use
Sans Serif

Colors
0255a3
ffffff
000000
f78f20
b1b1b1
9d9d9d
1b1b1b
33a6d7
ec1f27

Requirements
Must have
• My logo on one side maybe with a some kind of background on the other side all my information
Nice to have
• Some kind of background pictures provided by you .PLEASE HAVE ACCOUNT WITH PIXELVAULT WILL NOT PAY ANY EXTRA FEES .
Should not have
• Any kind of hamer, nails,screws, helmets itp. Please do not copy the other designs come up with something new.

```html
<!DOCTYPE html>
<html lang="en">
<head>
<meta charset="utf-8">
<title>Velmar Construction LLC – Business Card</title>
<link rel="stylesheet" href="https://fonts.googleapis.com/css2?family=Saira:wght@400;500;600;700&display=swap">
<style>
  :root {
    --backdrop: #4a3426;
    --card: #ffffff;
    --ink: #1b1b1b;
    --black: #000000;
    --orange: #f78f20;
    --band: #ec9a24;
    --rule: #9d9d9d;
    --shadow: rgba(0, 0, 0, 0.45);
  }
  * { box-sizing: border-box; margin: 0; padding: 0; }
  html, body {
    width: 1200px;
    height: 1195px;
    overflow: hidden;
    background: var(--backdrop);
    font-family: "Saira", sans-serif;
  }
  .canvas { position: relative; width: 1200px; height: 1195px; }

  .card {
    position: absolute;
    left: 290px;
    width: 620px;
    height: 372px;
    background: var(--card);
    box-shadow: 0 18px 22px -10px var(--shadow);
    overflow: hidden;
  }
  .card--front { top: 162px; }
  .card--back  { top: 673px; }

  .card__band {
    position: absolute;
    left: 0; right: 0; bottom: 0;
    height: 36px;
    background: var(--band);
    color: var(--card);
    display: flex;
    align-items: center;
    justify-content: center;
    font-weight: 600;
  }
  .card--front .card__band { font-size: 16px; letter-spacing: 0.6px; }
  .card--back .card__band { font-size: 17px; letter-spacing: 3.2px; }

  /* wordmark */
  .wordmark {
    position: absolute;
    display: flex;
    align-items: center;
    color: var(--ink);
    font-weight: 600;
    line-height: 1;
  }
  .wordmark__square { background: var(--orange); flex: none; }
  .wordmark__name { display: flex; flex-direction: column; }
  .wordmark__title { text-transform: uppercase; }
  .wordmark__sub { text-transform: uppercase; }

  .card--front .wordmark { left: 188px; top: 68px; gap: 10px; }
  .card--front .wordmark__square { width: 18px; height: 18px; }
  .card--front .wordmark__title { font-size: 54px; letter-spacing: 4px; }
  .card--front .wordmark__sub { font-size: 17px; letter-spacing: 2.2px; margin-top: 2px; }

  .card--back .wordmark { left: 100px; top: 120px; gap: 18px; }
  .card--back .wordmark__square { width: 34px; height: 34px; }
  .card--back .wordmark__title { font-size: 100px; letter-spacing: 7px; }
  .card--back .wordmark__sub { font-size: 31px; letter-spacing: 4.2px; margin-top: 4px; }

  /* person */
  .person {
    position: absolute;
    right: 335px;
    top: 236px;
    text-align: right;
  }
  .person__name { color: var(--orange); font-size: 21px; font-weight: 400; line-height: 1.2; }
  .person__role { color: var(--ink); font-size: 14px; font-weight: 400; margin-top: 2px; }

  .divider {
    position: absolute;
    left: 316px;
    top: 202px;
    width: 2px;
    height: 116px;
    background: linear-gradient(to bottom, transparent, var(--rule) 30%, var(--rule) 70%, transparent);
  }

  .contacts {
    position: absolute;
    left: 345px;
    top: 220px;
    list-style: none;
  }
  .contacts__item {
    display: flex;
    align-items: center;
    height: 20px;
    margin-bottom: 10.5px;
    font-size: 14.5px;
    color: var(--ink);
  }
  .contacts__icon { width: 18px; height: 16px; margin-right: 7px; flex: none; }
</style>
</head>
<body>
<main class="canvas">

  <section class="card card--front" aria-label="Business card, information side">
    <div class="wordmark">
      <span class="wordmark__square"></span>
      <div class="wordmark__name">
        <span class="wordmark__title">Velmar</span>
        <span class="wordmark__sub">Construction LLC</span>
      </div>
    </div>

    <div class="person">
      <p class="person__name">Gerald Tomasino</p>
      <p class="person__role">Chief Operating Officer</p>
    </div>

    <div class="divider"></div>

    <ul class="contacts">
      <li class="contacts__item">
        <svg class="contacts__icon" viewBox="0 0 18 16" aria-hidden="true">
          <path d="M2 6 Q9 0 16 6 L14 8 L12 6 L12 5 Q9 4 6 5 L6 6 L4 8 Z" fill="#f78f20"/>
          <rect x="4" y="8" width="10" height="6" rx="1" fill="#f78f20"/>
          <circle cx="9" cy="11" r="1.6" fill="#fff"/>
        </svg>
        555-318-6094
      </li>
      <li class="contacts__item">
        <svg class="contacts__icon" viewBox="0 0 18 16" aria-hidden="true">
          <rect x="5" y="0.8" width="8" height="14.4" rx="1.5" fill="none" stroke="#f78f20" stroke-width="1.4"/>
          <line x1="8" y1="13" x2="10" y2="13" stroke="#f78f20" stroke-width="1.2"/>
        </svg>
        555-742-0583
      </li>
      <li class="contacts__item">
        <svg class="contacts__icon" viewBox="0 0 18 16" aria-hidden="true">
          <rect x="1" y="3" width="16" height="11" fill="#f78f20"/>
          <path d="M1 3 L9 10 L17 3 M1 14 L7 8.5 M17 14 L11 8.5" fill="none" stroke="#fff" stroke-width="1"/>
        </svg>
        velmarllc@tridomail.com
      </li>
    </ul>

    <div class="card__band">418 harbor 87th. Dunmoor park ny 10352</div>
  </section>

  <section class="card card--back" aria-label="Business card, logo side">
    <div class="wordmark">
      <span class="wordmark__square"></span>
      <div class="wordmark__name">
        <span class="wordmark__title">Velmar</span>
        <span class="wordmark__sub">Construction LLC</span>
      </div>
    </div>

    <div class="card__band">www.velmarllc.com</div>
  </section>

</main>
</body>
</html>
```